Redesign of Plastic Surgeon Website to fully responsive / modern feel

Hi

Our current website is out of date www.harbourlinecosmetic.org

We want a fresh / modern looking design
Needs to be fully responsive design that works extremely well on ipad and mobile device

Would like design for both full screen website and mobile

Have listed a few websites of other plastic surgeons we like
http://www.reformclinicdaily.com/
http://www.peterholtbymd.com/
http://www.corvanbeauty.com/
http://www.tidewellcontouring.com/

Menu needs to include
1. About Us
2. Procedures (see current website for example)
3. News
4. Patient Resources
5. Contact Us

We are flexible with colours / images / layout

I have uploaded a document that has some content - the face pages content is completed only

some of the procedures can have content upwards of 4000 words - total website can be large with over 40,000 words
Updates

Target Market(s)

Mainly women 20-60 85% of practice
Some men 15%

Industry/Entity Type

Plastic Surgery

Number of Pages Required

5+ page

Requirements
Must have
• We need designs for
• Homepage
• Internal pages
• 1. Landing pages for breast / body / face / non surgical main pages
• 2. Procedure pages for individual pages under each section - eg breast augmentation
• 3. About us pages - like meet the doctor, our staff, clinics
• 4. Contact page
• 5. Blog / News page
Nice to have
• See our list of websites for examples of designs we like
• Like full screen design with nice hero image
• Needs to have good to call to action messages on home page like
• Specials, procedure of the month, etc

```html
<!DOCTYPE html>
<html lang="en">
<head>
<meta charset="utf-8">
<title>Harbourline Institute of Plastic Surgery</title>
<link href="https://fonts.googleapis.com/css2?family=Alegreya+Sans:wght@300;400;500&display=swap" rel="stylesheet">
<style>
:root{
  --rose:#c4585a;
  --plum:#7e3d72;
  --cat-red:#c95b5b;
  --cat-blue:#5c9fd2;
  --cat-green:#4fc79b;
  --cat-violet:#9a5dd0;
  --charcoal:#2f2a2a;
  --paper:#ececec;
  --ink:#3d3d3d;
  --panel:#444;
  --white:#fff;
}
*{box-sizing:border-box;margin:0;padding:0}
html,body{width:1200px;height:2250px;overflow:hidden}
body{position:relative;font-family:"Alegreya Sans",sans-serif;color:var(--ink);background:var(--paper)}
.abs{position:absolute}

/* header */
.site-header{left:0;top:0;width:1200px;height:105px;background:#f7f7f7}
.brand{display:flex;align-items:center;gap:8px;white-space:nowrap}
.site-header .brand{left:100px;top:37px}
.brand-mark{width:26px;height:26px;border-radius:50%;border:1.5px solid var(--rose);flex:none}
.brand-name{font-size:18px;font-weight:300;color:var(--ink)}
.main-nav{left:318px;top:44px;display:flex;font-size:13px;text-transform:uppercase;color:#555;letter-spacing:.3px;white-space:nowrap}
.main-nav a{color:inherit;text-decoration:none;margin-right:27px}
.main-nav a:last-child{margin-right:0}
.main-nav a.current{color:var(--rose);border-bottom:1.5px solid var(--rose);padding-bottom:6px}
.call-btn{background:var(--rose);color:var(--white);display:flex;align-items:center;justify-content:center;gap:9px;width:225px;height:30px;white-space:nowrap}
.call-btn small{font-size:8px;text-transform:uppercase}
.call-btn strong{font-size:17px;font-weight:500}
.site-header .call-btn{left:873px;top:38px}

/* hero */
.hero{left:0;top:105px;width:1200px;height:645px;background:linear-gradient(90deg,#e4c4ad 0%,#f2dccb 25%,#e9cdb8 50%,#ecd3bf 72%,#f4e6d2 100%)}
.hero-title{left:0;top:200px;width:1200px;text-align:center;font-size:40px;font-weight:300;color:var(--rose);text-transform:uppercase}
.hero-sub{left:0;top:250px;width:1200px;text-align:center;font-size:15px;color:#444}
.hero-btn{top:287px;width:102px;height:26px;font-size:12px;text-transform:uppercase;display:flex;align-items:center;justify-content:center}
.hero-btn.solid{left:490px;background:var(--rose);color:var(--white)}
.hero-btn.outline{left:607px;border:1px solid #555;color:#444}
.promo{top:463px;width:225px;height:107px;display:flex;align-items:center;justify-content:center;text-align:center;color:var(--white);font-size:20px;line-height:27px;text-transform:uppercase}
.promo.month{left:100px;background:rgba(196,79,72,.92)}
.promo.sculpt{left:358px;background:rgba(63,142,168,.92)}
.promo.doctor{left:616px;background:rgba(58,174,130,.92)}
.promo.specials{left:873px;background:rgba(140,92,194,.95)}

/* welcome */
.welcome{left:0;top:750px;width:1200px;height:240px;background:var(--plum);color:var(--white)}
.section-title{width:100%;text-align:center;font-size:40px;font-weight:300;text-transform:uppercase}
.welcome .section-title{position:absolute;top:35px}
.welcome p{position:absolute;top:102px;font-size:14px;line-height:19.5px}
.welcome .col-left{left:100px;width:472px}
.welcome .col-right{left:607px;width:488px}

/* categories */
.category{top:990px;width:300px;height:255px;color:var(--white);text-align:center}
.category h3{margin-top:55px;font-size:21px;font-weight:400;text-transform:uppercase}
.category ul{list-style:none;margin-top:14px;font-size:15px;line-height:19px}
.category.face{left:0;background:linear-gradient(135deg,#d26e66,var(--cat-red))}
.category.breast{left:300px;background:linear-gradient(135deg,#6aaedb,var(--cat-blue))}
.category.body{left:600px;background:linear-gradient(135deg,#5dd3a6,var(--cat-green))}
.category.nonsurgical{left:900px;background:linear-gradient(135deg,#a86ad8,var(--cat-violet))}

/* affiliations */
.affiliations{left:0;top:1245px;width:1200px;height:255px;background:var(--charcoal);color:var(--white)}
.affiliations .section-title{position:absolute;top:50px}
.badge{position:absolute;background:#8a8585}

/* contact */
.contact-title{left:0;top:1550px;color:#555}
.contact-sub{left:0;top:1597px;width:1200px;text-align:center;font-size:15px;color:#444}
.field{border:1px solid #777;font-size:17px;font-weight:300;color:#aaa;padding:12px}
.field.filled{color:#666}
.send-btn{left:100px;top:1929px;width:390px;height:48px;background:var(--rose);color:var(--white);font-size:17px;text-transform:uppercase;display:flex;align-items:center;justify-content:center}
.divider{left:600px;top:1732px;width:1px;height:148px;background:#777}
.clinic-open{left:708px;top:1672px;width:390px;height:161px;background:var(--white);border:1px solid #999;padding:12px}
.clinic-open h4{font-size:17px;font-weight:300;color:#666}
.clinic-open address{font-style:normal;margin-top:18px;font-size:12px;line-height:15px;color:#444}
.clinic-row{left:708px;width:390px;height:48px;background:var(--panel);color:#ddd;font-size:17px;font-weight:300;padding:12px;border-bottom:1px solid #666}

/* footer */
.footer-rule{left:100px;top:2039px;width:998px;height:1px;background:#777}
.footer-brand{left:100px;top:2124px}
.copyright{left:100px;top:2197px;font-size:9px;color:#444}
.copyright span{color:var(--rose)}
.footer-col h5{font-size:17px;font-weight:300;color:#666;text-align:center;margin-bottom:8px}
.sitemap{left:511px;top:2083px;width:120px;text-align:center;font-size:12px;line-height:16px}
.sitemap .current{color:var(--rose)}
.posts{left:660px;top:2083px;width:165px}
.post{font-size:12px;line-height:13px;margin-bottom:6px;white-space:nowrap}
.post small{display:block;font-size:7px;color:var(--rose)}
.footer .call-btn{left:873px;top:2088px}
.social{top:2148px;width:38px;height:38px;border-radius:50%;background:var(--charcoal)}
.social.accent{background:var(--rose)}
</style>
</head>
<body>

<header class="site-header abs">
  <div class="brand abs"><span class="brand-mark"></span><span class="brand-name">Harbourline Institute</span></div>
  <nav class="main-nav abs">
    <a class="current" href="#">Home</a><a href="#">About Us</a><a href="#">Procedures</a><a href="#" style="margin-right:20px">Patient Resources</a><a href="#" style="margin-right:20px">News</a><a href="#">Contact Us</a>
  </nav>
  <div class="call-btn abs"><small>Call for appointments</small><strong>02 8000 4417</strong></div>
</header>

<section class="hero abs" role="img" aria-label="Hero photograph of three women's faces showing youth to maturity">
  <h1 class="hero-title abs">Your Future Looks Beautiful</h1>
  <p class="hero-sub abs">At the Institute of Aesthetic Plastic Surgery</p>
  <a class="hero-btn solid abs">Learn More</a>
  <a class="hero-btn outline abs">Contact Us</a>
  <a class="promo month abs">Procedure of<br>the Month</a>
  <a class="promo sculpt abs">CryoContour<br>SonoForm</a>
  <a class="promo doctor abs">Meet<br>Dr.Whitcombe</a>
  <a class="promo specials abs">Specials of<br>Harbourline Institute</a>
</section>

<section class="welcome abs">
  <h2 class="section-title">Welcome</h2>
  <p class="col-left">You can expect beautiful results at the Institute of Aesthetic Plastic Surgery.<br>Offering unparalleled expertise in face, breast and body enhancement,<br>including facelifts, breast augmentation / lift / reduction or tummy tucks,<br>we offer total care at every step of your transformative journey.</p>
  <p class="col-right">Dr Whitcombe is one of Australia's most eminent specialists in plastic and cosmetic surgery, and is supported by our highly qualified, professional team.<br>As Sydney's premier plastic surgery clinic, we use only the most revolutionary techniques to minimise scarring to help you look better, feel better and enjoy a beautiful new you.</p>
</section>

<div class="category face abs" role="img" aria-label="Photograph of a woman touching her face, tinted red">
  <h3>Face</h3>
  <ul><li>Facelift</li><li>Rhinoplasty</li><li>Blepharoplasty</li><li>Browlift</li><li>Otoplasty</li></ul>
</div>
<div class="category breast abs" role="img" aria-label="Photograph of a woman's shoulders, tinted blue">
  <h3>Breast</h3>
  <ul><li>Breast Augmentation</li><li>Breast Lift</li><li>Breast Lift with Implants</li><li>Breast Reduction</li><li>Gynaecomastia</li><li>Mummy Makeover</li></ul>
</div>
<div class="category body abs" role="img" aria-label="Photograph of a woman's waist, tinted green">
  <h3>Body</h3>
  <ul><li>Tummy Tuck</li><li>Labiaplasty</li><li>Liposuction</li><li>Brazilian Butt Lift</li><li>Mummy Makeover</li></ul>
</div>
<div class="category nonsurgical abs" role="img" aria-label="Photograph of a woman with hands framing her face, tinted violet">
  <h3>Non Surgical</h3>
  <ul><li>Anti Wrinkle</li><li>Dermal Fillers</li><li>CryoContour</li><li>SonoForm</li><li>VeloTone</li></ul>
</div>

<section class="affiliations abs">
  <h2 class="section-title">Affiliations</h2>
  <div class="badge" style="left:102px;width:52px;height:52px;top:140px;border-radius:50%" role="img" aria-label="Partner society badge"></div>
  <div class="badge" style="left:325px;width:30px;height:30px;top:150px;border-radius:50%" role="img" aria-label="Partner society badge"></div>
  <div class="badge" style="left:445px;width:135px;height:46px;top:142px" role="img" aria-label="Partner society badge"></div>
  <div class="badge" style="left:655px;width:52px;height:52px;top:140px" role="img" aria-label="Partner society badge"></div>
  <div class="badge" style="left:797px;width:70px;height:40px;top:146px" role="img" aria-label="Partner society badge"></div>
  <div class="badge" style="left:935px;width:165px;height:50px;top:140px" role="img" aria-label="College fellowship badge"></div>
</section>

<section class="contact">
  <h2 class="section-title contact-title abs">Contact Form</h2>
  <p class="contact-sub abs">Do write us on our contact form for any details you may be interested on.</p>
  <div class="field abs" style="left:100px;top:1672px;width:187px;height:48px">First Name</div>
  <div class="field filled abs" style="left:303px;top:1672px;width:187px;height:48px">Ellison</div>
  <div class="field abs" style="left:100px;top:1737px;width:390px;height:48px">Email Address</div>
  <div class="field abs" style="left:100px;top:1801px;width:390px;height:112px">Message</div>
  <div class="send-btn abs">Send Message</div>
  <div class="divider abs"></div>
  <div class="clinic-open abs">
    <h4>Northvale</h4>
    <address>Marlow Clinic<br>Suite 204<br>12 Ferrel Street<br>Northvale 2071</address>
  </div>
  <div class="clinic-row abs" style="top:1833px">Eastmere</div>
  <div class="clinic-row abs" style="top:1881px">Cliffton</div>
  <div class="clinic-row abs" style="top:1929px">Baywood</div>
</section>

<footer class="footer">
  <div class="footer-rule abs"></div>
  <div class="brand footer-brand abs"><span class="brand-mark"></span><span class="brand-name">Harbourline Institute</span></div>
  <p class="copyright abs">© Copyright 2016. <span>Harbourline Institute of Plastic Surgery</span>. All rights reserved.</p>
  <div class="footer-col sitemap abs">
    <h5>Sitemap</h5>
    <div class="current">Home</div><div>About Us</div><div>Procedures</div><div>Patient Resources</div><div>News</div><div>Contact Us</div>
  </div>
  <div class="footer-col posts abs">
    <h5>Last Posts</h5>
    <div class="post">Lorem ipsum dolors met aqui...<small>January 14th, 2016</small></div>
    <div class="post">Lorem ipsum dolors met aqui...<small>January 9th, 2016</small></div>
    <div class="post">Lorem ipsum dolors met aqui...<small>December 28th, 2015</small></div>
  </div>
  <div class="call-btn abs"><small>Call for appointments</small><strong>02 8000 4417</strong></div>
  <span class="social abs" style="left:903px" aria-label="Social link"></span>
  <span class="social accent abs" style="left:965px" aria-label="Social link"></span>
  <span class="social abs" style="left:1029px" aria-label="Social link"></span>
</footer>

</body>
</html>
```